Mobile Home Page Design for “Zarvo for Plumbers” – in Figma

PipeDashly: Fast, Reliable Emergency Plumbing at Your Fingertips

PipeDashly is a streamlined platform connecting homeowners with trusted, local plumbers for urgent repairs—whether it’s a burst pipe, leak, or blocked toilet. Designed for speed and peace of mind, our homepage will be clean, modern, and mobile-optimized to guide users from problem to solution in minutes.

Our primary users are homeowners in stressful situations who care most about price transparency and how fast help can arrive. Bookings are made exclusively online, so the user experience must instill confidence and eliminate hesitation.

The call-to-action should be immediate and persuasive—"See Prices & Book" will be prominently featured as the main CTA. Additional trust-builders could include:

A simple 3-step booking illustration (Tell us what’s wrong → See prices → Get a plumber)
Customer reviews or “Trusted by 10,000+ homeowners” badges

Display real-time availability ("Next plumber available in 40 minutes")
Price estimates upfront—with clear service types

Target Market(s)

Home Owners: 35-65 Years old.

Industry/Entity Type

Home Services.

Number of Pages Required

1 page

Font styles to use
Sans Serif

Colors
0054AA
0677BA
7BADD7
CADEEF
E8F1F8
FFF300
FFF600
FEFA6F
FFFEC7
FFFEE8

Requirements
Nice to have
• Map showing that plumbers are nearby. Trustworthy look and feel. Blue/Red or Blue/Yellow.

```html
<!DOCTYPE html>
<html lang="en">
<head>
<meta charset="utf-8">
<title>PipeDashly – Mobile Home</title>
<link href="https://fonts.googleapis.com/css2?family=Ubuntu:wght@500;700&family=Roboto:wght@400;500;700&display=swap" rel="stylesheet">
<style>
:root{
  --blue:#1a5fe0;
  --blue-bright:#3d84f5;
  --blue-soft:#4b8af5;
  --yellow:#fff300;
  --yellow-soft:#fffec7;
  --ink:#22252b;
  --dark:#2b2d33;
  --dark-2:#3a3d44;
  --muted:#6b6f78;
  --line:#dcdfe5;
  --pale:#eef3fc;
  --white:#ffffff;
}
*{box-sizing:border-box;margin:0;padding:0}
html,body{width:1200px;height:4068px;overflow:hidden;background:var(--white)}
body{position:relative;font-family:Roboto,Arial,sans-serif;color:var(--ink)}
h1,h2,h3,h4{font-family:Ubuntu,Arial,sans-serif;font-weight:700}
.col{position:absolute;width:389px;border:1px solid var(--line);overflow:hidden;background:var(--white)}
.col-left{left:103px;top:19px}
.col-right{left:719px;top:34px}
section{position:relative}
.label{display:flex;align-items:center;gap:7px;font:700 13px Roboto,sans-serif;color:var(--blue);letter-spacing:.3px}
.label.light{color:#fff}
.label svg{width:15px;height:15px}
.sec-title{font-size:25px;line-height:31px;color:var(--ink)}
.light-title{color:#fff}
.body-text{font-size:11.5px;line-height:20px;color:var(--muted)}
.more{font:700 11.5px Roboto,sans-serif;color:var(--blue);display:flex;gap:5px;align-items:center}
.circle-sm{width:18px;height:18px;border:1.3px solid currentColor;border-radius:50%;display:inline-block}

/* hero */
.hero{height:517px}
.hero-photo{position:absolute;inset:0;background:linear-gradient(135deg,#5c7fd0 0%,#3e63c4 45%,#8aa8e6 75%,#4a6cc8 100%)}
.topbar{position:absolute;left:0;right:0;top:0;height:62px;background:var(--dark);color:#fff;font-size:10.5px;text-align:center;padding-top:8px}
.topbar .row{display:flex;justify-content:center;gap:14px}
.topbar .soc{display:flex;justify-content:center;gap:14px;margin-top:10px;color:#fff}
.nav{position:absolute;left:9px;right:9px;top:62px;height:62px;background:#f3f6fc;border-radius:0 0 6px 6px;display:flex;align-items:center;justify-content:space-between;padding:0 16px}
.brand{font:700 17px Ubuntu,sans-serif;color:var(--blue)}
.burger span{display:block;width:28px;height:2px;background:var(--blue);margin:6px 0}
.hero h1{position:absolute;top:228px;left:0;right:0;text-align:center;color:#fff;font-size:27px;line-height:34px}
.hero p{position:absolute;top:308px;left:8px;right:8px;text-align:center;color:#fff;font-size:11.5px;line-height:24px}
.pill{display:inline-flex;align-items:center;justify-content:center;gap:8px;background:#fff;color:var(--blue);border-radius:24px;font:500 11.5px Roboto,sans-serif}
.hero .pill{position:absolute;top:368px;left:109px;width:170px;height:46px;background:var(--yellow);color:var(--ink);font-weight:700}
.arrows{position:absolute;top:453px;left:0;right:0;display:flex;justify-content:center;gap:16px}
.arrows span{width:38px;height:38px;border-radius:50%;background:rgba(255,255,255,.35);display:flex;align-items:center;justify-content:center;color:#fff;font-size:14px}

/* about */
.about{height:609px}
.about .label{position:absolute;left:9px;top:72px}
.about h2{position:absolute;left:9px;top:101px;width:360px}
.about-stripe{position:absolute;left:14px;top:195px;width:300px;height:265px;background:var(--blue);transform:skewX(-4deg)}
.about-photo{position:absolute;left:44px;top:187px;width:302px;height:284px;background:linear-gradient(160deg,#d9dde3,#9fb0c8 55%,#3b5a9a)}
.about .body-text{position:absolute;left:9px;right:6px;top:512px;font-size:11px}

/* service cards */
.cards{padding:0 9px}
.card{height:232px;text-align:center;padding-top:26px}
.card svg{width:52px;height:52px}
.card h3{font-size:15px;margin-top:16px}
.card p{font-size:11.5px;line-height:20px;margin:8px 14px 0}
.card .more{justify-content:center;margin-top:18px}
.card.dark{background:var(--dark);color:#fff}
.card.dark .more{color:#fff}
.card.blue{background:var(--blue-soft);color:#fff}
.card.blue .more{color:#fff}
.card.plain p{color:var(--muted)}
.card.plain h3{color:var(--ink)}

/* why */
.why{height:802px;background:var(--dark);color:#fff}
.why .label{position:absolute;left:9px;top:44px}
.why .label svg{color:var(--yellow)}
.why h2{position:absolute;left:9px;top:74px;width:370px}
.why-line{position:absolute;left:24px;top:200px;height:230px;border-left:1.5px dashed #8a8d94}
.why-item{position:absolute;left:56px;right:8px}
.why-item h4{font:700 15px Roboto,sans-serif}
.why-item p{font-size:11.5px;line-height:20px;margin-top:10px;color:#e5e7ea}
.why-photo{position:absolute;left:9px;top:480px;width:370px;height:312px;background:linear-gradient(135deg,#e7e7e9,#b9bcc3 50%,#34456e)}

/* process */
.process{height:1380px}
.process h2{position:absolute;top:58px;left:0;right:0;text-align:center;font-size:24px}
.step{position:absolute;left:0;right:0;height:317px;text-align:center}
.step .icon{width:56px;height:56px;border-radius:50%;margin:0 auto;background:#fff;box-shadow:0 4px 14px rgba(40,60,120,.12);display:flex;align-items:center;justify-content:center}
.step .icon svg{width:36px;height:36px}
.step .rule{position:absolute;top:68px;left:107px;width:174px;border-top:2px solid #8a8d94}
.step .tri{position:absolute;top:69px;left:188px;border:7px solid transparent;border-top:8px solid #6b6f78}
.step .disc{position:absolute;top:90px;left:111px;width:167px;height:167px;border-radius:50%;background:#fff;box-shadow:0 6px 22px rgba(40,60,120,.13);padding-top:18px}
.step .num{font:500 30px Ubuntu,sans-serif;color:#fff;-webkit-text-stroke:1.2px #8a8d94}
.step h4{font-size:16px;margin-top:4px}
.step p{font-size:11.5px;line-height:20px;color:var(--muted);margin:6px 28px 0}

/* mission */
.mission{height:247px;background:radial-gradient(circle at 78% 30%,#3f86f2,#1657d8 60%);text-align:center;color:#fff}
.mission h2{position:absolute;top:50px;left:6px;right:6px;font-size:24px;line-height:33px}
.mission .pill{position:absolute;top:138px;left:114px;width:160px;height:44px;border-radius:6px;font-size:11.5px}

/* services */
.services{height:1348px}
.services .label{position:absolute;top:66px;left:0;right:0;justify-content:center}
.services h2{position:absolute;top:98px;left:0;right:0;text-align:center;font-size:25px}
.svc{position:absolute;left:0;right:0;height:397px}
.svc .photo{position:absolute;left:96px;top:0;width:196px;height:196px;border-radius:50%;background:linear-gradient(150deg,#e9ecf1,#9fb2d3 50%,#2f4f9a)}
.svc .badge{position:absolute;left:234px;top:0;width:62px;height:62px;border-radius:50%;background:#fff;box-shadow:0 3px 10px rgba(0,0,0,.1);display:flex;align-items:center;justify-content:center}
.svc .badge svg{width:28px;height:28px}
.svc h3{position:absolute;left:56px;top:227px;font-size:16px}
.svc .body-text{position:absolute;left:56px;right:50px;top:258px;font-size:11.5px;line-height:24px}
.svc .more{position:absolute;left:56px;top:341px}

/* faq */
.faq{height:1061px;background:var(--dark)}
.faq .label{position:absolute;left:9px;top:54px}
.faq h2{position:absolute;left:9px;top:85px;color:#fff}
.q{position:absolute;left:9px;width:370px;border-radius:3px;color:#fff;font:700 15px Ubuntu,sans-serif;padding:0 16px}
.q.open{top:147px;height:133px;background:var(--blue-bright);padding-top:19px}
.q.open p{font:400 11.5px/20px Roboto,sans-serif;margin-top:30px;padding-left:8px}
.q.closed{height:56px;background:var(--dark-2);display:flex;align-items:center}
.book{position:absolute;left:9px;top:547px;width:370px;height:500px;border-radius:4px;background:linear-gradient(180deg,#3f86f4,#1c62e2);padding:28px 16px 0;color:#fff}
.book h3{font:700 18px Ubuntu,sans-serif}
.field{font-size:12px;height:60px;padding-top:20px;border-bottom:1px dashed rgba(255,255,255,.6)}
.field.tall{height:106px}
.book .pill{position:absolute;left:16px;right:16px;bottom:30px;height:38px;border-radius:5px;font-size:11.5px}

/* testimonial */
.testi{height:528px}
.testi .box{position:absolute;left:9px;right:9px;top:0;bottom:8px;background:var(--pale);text-align:center}
.testi .label{position:absolute;top:64px;left:0;right:0;justify-content:center}
.testi h2{position:absolute;top:96px;left:0;right:0;font-size:25px}
.testi .body-text{position:absolute;top:152px;left:18px;right:18px;font-size:12.5px;line-height:26px;color:#555}
.testi h4{position:absolute;top:419px;left:0;right:0;font:700 15px Roboto,sans-serif}
.testi .role{position:absolute;top:446px;left:0;right:0;font-size:11.5px;color:var(--blue)}

/* footer */
.footer{height:739px;background:var(--dark);color:#fff}
.footer .brand{position:absolute;left:50px;top:60px;color:var(--blue-bright)}
.call{position:absolute;left:187px;top:58px;display:flex;align-items:center;gap:8px}
.call .ph{width:36px;height:36px;border-radius:50%;background:var(--blue);display:flex;align-items:center;justify-content:center}
.call small{display:block;font-size:9px}
.call b{font-size:11.5px}
.footer .soc{position:absolute;top:116px;left:0;right:0;display:flex;justify-content:center;gap:12px}
.footer .soc .circle-sm{width:24px;height:24px}
.hr{position:absolute;left:9px;right:9px;border-top:1px solid #4a4d55}
.footer h4{position:absolute;left:9px;font:700 15px Ubuntu,sans-serif}
.hours{position:absolute;left:9px;right:9px;display:flex;justify-content:space-between;font-size:11.5px;height:56px;border-bottom:1px dashed #5a5d65}
.post{position:absolute;left:9px;right:9px;display:flex;gap:14px}
.post .thumb{width:62px;height:62px;flex:none;background:linear-gradient(135deg,#e6e9ee,#8ea3c9)}
.post b{font-size:11.5px;line-height:17px;display:block}
.post small{font-size:10px;display:block;margin-top:6px}
.links{position:absolute;top:677px;left:0;right:0;display:flex;justify-content:center;gap:22px;font-size:11.5px}
.copy{position:absolute;top:706px;left:0;right:0;text-align:center;font-size:11.5px}
.totop{position:absolute;right:14px;top:686px;width:36px;height:36px;border-radius:50%;border:1.5px solid var(--blue);display:flex;align-items:center;justify-content:center}
</style>
</head>
<body>

<div class="col col-left">

  <section class="hero">
    <div class="hero-photo" role="img" aria-label="Photo of a plumber's hands tightening a chrome kitchen tap with a wrench, blue tint"></div>
    <div class="topbar">
      <div class="row"><span>☎ +100 555 0102</span><span>✉ hello@pipedashly.example</span><span>⌖ United State&nbsp; State</span></div>
      <div class="soc"><span class="circle-sm"></span><span class="circle-sm"></span><span class="circle-sm"></span><span class="circle-sm"></span></div>
    </div>
    <div class="nav">
      <span class="brand">PipeDashly</span>
      <div class="burger"><span></span><span></span><span></span></div>
    </div>
    <h1>Plumbing solutions that<br>flow smoothly</h1>
    <p>Shut off the water supply to your home immediately and call an emergency plumber for assistance.</p>
    <span class="pill">SEE PRICES &amp; BOOK</span>
    <div class="arrows"><span>←</span><span>→</span></div>
  </section>

  <section class="about">
    <div class="label"><svg viewBox="0 0 16 16" fill="none" stroke="currentColor" stroke-width="1.3"><path d="M3 13l6-6M9 7a3 3 0 104-4l-2 2-2-2 2-2"/></svg>ABOUT US</div>
    <h2 class="sec-title">Swift Solutions for All Your Plumbing Predicaments</h2>
    <div class="about-stripe"></div>
    <div class="about-photo" role="img" aria-label="Photo of a smiling plumber in cap holding a red wrench beside a sink trap"></div>
    <p class="body-text">It's important to hire a plumber who is properly licensed and qualified to do work. This ensures that they have the necessary skills and knowledge and catch potential issues before they become major problems.</p>
  </section>

  <section class="cards">
    <div class="card dark">
      <svg viewBox="0 0 52 52" fill="none" stroke="#fff" stroke-width="1.6"><rect x="14" y="6" width="24" height="40" rx="3"/><circle cx="26" cy="18" r="5"/><path d="M20 32h12M20 38h12M8 14v24M44 14v24"/></svg>
      <h3>Water Heater Installation &amp; Repair</h3>
      <p>Avoid putting grease, hair, or large objects down drains, and consider using drain covers to catch debris.</p>
      <div class="more">READ MORE →</div>
    </div>
    <div class="card blue">
      <svg viewBox="0 0 52 52" fill="none" stroke="#fff" stroke-width="1.6"><circle cx="24" cy="28" r="16"/><path d="M24 18v10l7 5"/><circle cx="38" cy="12" r="7" fill="#fff300" stroke="#fff300"/></svg>
      <h3>24/7 Emergency Plumbing Service</h3>
      <p>Avoid putting grease, hair, or large objects down drains, and consider using drain covers to catch debris.</p>
      <div class="more">READ MORE →</div>
    </div>
    <div class="card plain">
      <svg viewBox="0 0 52 52" fill="none" stroke="#1a5fe0" stroke-width="1.6"><path d="M10 16h32l-4 10H14z"/><rect x="14" y="26" width="24" height="18"/><path d="M20 8h12v8M20 32l6 8 6-8"/></svg>
      <h3>Garbage Disposal Repair &amp; Installation</h3>
      <p>The duration depends on the complexity covers of the issue. Simple be completed problems.</p>
      <div class="more">READ MORE →</div>
    </div>
  </section>

  <section class="why">
    <div class="label light"><svg viewBox="0 0 16 16" fill="none" stroke="currentColor" stroke-width="1.3"><path d="M3 13l6-6M9 7a3 3 0 104-4l-2 2-2-2 2-2"/></svg>WHY CHOOSE US</div>
    <h2 class="sec-title light-title">From drip to drain we've got you covered</h2>
    <div class="why-line"></div>
    <div class="why-item" style="top:172px"><h4>Pipe Installation &amp; Repair</h4><p>Signs include low water pressure, unusual noises slow drainage, or visible leaks.</p></div>
    <div class="why-item" style="top:273px"><h4>Kitchen Plumbing Services</h4><p>Signs include low water pressure, unusual noises slow drainage, or visible leaks.</p></div>
    <div class="why-item" style="top:374px"><h4>Your Water Woes Our Expertise</h4><p>Signs include low water pressure, unusual noises slow drainage, or visible leaks.</p></div>
    <div class="why-photo" role="img" aria-label="Photo of a plumber in overalls fixing a kitchen sink tap"></div>
  </section>

  <section class="process">
    <h2>Standard Working Process</h2>
    <div class="step" style="top:120px">
      <div class="icon"><svg viewBox="0 0 36 36" fill="none" stroke="#1a5fe0" stroke-width="1.6"><path d="M8 6v10a10 10 0 0020 0V6M14 6v10a4 4 0 008 0V6M18 26v6"/></svg></div>
      <div class="rule"></div><div class="tri"></div>
      <div class="disc"><div class="num">01</div><h4>Tell Us The Issue</h4><p>Shut off the water supply to home immediately</p></div>
    </div>
    <div class="step" style="top:437px">
      <div class="icon"><svg viewBox="0 0 36 36" fill="none" stroke="#1a5fe0" stroke-width="1.6"><path d="M6 28h24M10 28V14h8v14M18 18h8v10M14 8v6"/></svg></div>
      <div class="rule"></div><div class="tri"></div>
      <div class="disc"><div class="num">02</div><h4>See Prices</h4><p>Shut off the water supply to home immediately</p></div>
    </div>
    <div class="step" style="top:754px">
      <div class="icon"><svg viewBox="0 0 36 36" fill="none" stroke="#1a5fe0" stroke-width="1.6"><path d="M8 30l10-10M20 18l8-8M24 6l6 6M10 10h8v6"/></svg></div>
      <div class="rule"></div><div class="tri"></div>
      <div class="disc"><div class="num">03</div><h4>Get A Plumber</h4><p>Shut off the water supply to home immediately</p></div>
    </div>
    <div class="step" style="top:1071px">
      <div class="icon"><svg viewBox="0 0 36 36" fill="none" stroke="#1a5fe0" stroke-width="1.6"><path d="M8 8h20v6H8zM15 14v16h6V14"/></svg></div>
      <div class="rule"></div><div class="tri"></div>
      <div class="disc"><div class="num">04</div><h4>Power flush</h4><p>Shut off the water supply to home immediately</p></div>
    </div>
  </section>
</div>

<div class="col col-right">

  <section class="mission">
    <h2>The mission is to provide Best Plumber</h2>
    <span class="pill">CONTACT NOW &nbsp;↗</span>
  </section>

  <section class="services">
    <div class="label"><svg viewBox="0 0 16 16" fill="none" stroke="currentColor" stroke-width="1.3"><path d="M3 13l6-6M9 7a3 3 0 104-4l-2 2-2-2 2-2"/></svg>SERVICES</div>
    <h2 class="sec-title">We Provide Service For You</h2>
    <div class="svc" style="top:156px">
      <div class="photo" role="img" aria-label="Photo of a plumber fitting a bathroom washbasin"></div>
      <div class="badge"><svg viewBox="0 0 28 28" fill="none" stroke="#1a5fe0" stroke-width="1.5"><rect x="6" y="8" width="16" height="14" rx="2"/><path d="M10 4v4M18 4v4M10 15h8"/></svg></div>
      <h3>Bathroom Remodeling</h3>
      <p class="body-text">Make sure the plumber you properly insured. This protects you in case any accidents or damage that may</p>
      <div class="more">READ MORE →</div>
    </div>
    <div class="svc" style="top:553px">
      <div class="photo" role="img" aria-label="Photo of a plumber repairing pipes under a sink"></div>
      <div class="badge"><svg viewBox="0 0 28 28" fill="none" stroke="#1a5fe0" stroke-width="1.5"><path d="M6 4v10h10v10M12 4v6h10"/></svg></div>
      <h3>Emergency Plumbing</h3>
      <p class="body-text">Make sure the plumber you properly insured. This protects you in case any accidents or damage that may</p>
      <div class="more">READ MORE →</div>
    </div>
    <div class="svc" style="top:950px">
      <div class="photo" role="img" aria-label="Photo of a plumber working on ceiling drain pipes"></div>
      <div class="badge"><svg viewBox="0 0 28 28" fill="none" stroke="#1a5fe0" stroke-width="1.5"><path d="M8 4v14a6 6 0 0012 0V4M13 4v14h2V4"/></svg></div>
      <h3>Drains Cleanning</h3>
      <p class="body-text">Make sure the plumber you properly insured. This protects you in case any accidents or damage that may</p>
      <div class="more">READ MORE →</div>
    </div>
  </section>

  <section class="faq">
    <div class="label light"><svg viewBox="0 0 16 16" fill="none" stroke="currentColor" stroke-width="1.3"><path d="M3 13l6-6M9 7a3 3 0 104-4l-2 2-2-2 2-2"/></svg>FAQ</div>
    <h2 class="sec-title">Questions Answer</h2>
    <div class="q open">1. What should I do if my is clogged?<p>Make sure the plumbing service offers is specific services you need. This could include everything from simple</p></div>
    <div class="q closed" style="top:297px">2. Can I use chemical drain cleaners?</div>
    <div class="q closed" style="top:370px">3. How do I if have plumbing leak?</div>
    <div class="q closed" style="top:442px">4. How do I know if a plumber?</div>
    <div class="book">
      <h3>Book And Appoinment</h3>
      <div class="field" style="padding-top:16px">Name *</div>
      <div class="field">Phone Number *</div>
      <div class="field">Email *</div>
      <div class="field">Subject</div>
      <div class="field tall">Message</div>
      <span class="pill">SEND MESSAGE &nbsp;↗</span>
    </div>
  </section>

  <section class="testi">
    <div class="box">
      <div class="label"><svg viewBox="0 0 16 16" fill="none" stroke="currentColor" stroke-width="1.3"><path d="M3 13l6-6M9 7a3 3 0 104-4l-2 2-2-2 2-2"/></svg>TESTIMONIAL</div>
      <h2 class="sec-title">Our Clients About Us</h2>
      <p class="body-text">Check online reviews and ask for recommendations from friends or family to gauge the reputation of the plumbing service. Positive reviews and testimonials can give you confidence in their reliability and quality of work</p>
      <h4>Marla Quinn</h4>
      <div class="role">Home Owner</div>
    </div>
  </section>

  <section class="footer">
    <span class="brand">PipeDashly</span>
    <div class="call">
      <span class="ph"><svg width="16" height="16" viewBox="0 0 16 16" fill="#fff"><path d="M3 2l3 0 1 3-2 1a8 8 0 004 4l1-2 3 1v3a1 1 0 01-1 1A12 12 0 012 3a1 1 0 011-1z"/></svg></span>
      <div><small>Requesting A Call:</small><b>(000) 555 010 200</b></div>
    </div>
    <div class="soc"><span class="circle-sm"></span><span class="circle-sm"></span><span class="circle-sm"></span><span class="circle-sm"></span></div>
    <div class="hr" style="top:167px"></div>
    <h4 style="top:204px">Working Hours:</h4>
    <div class="hours" style="top:244px"><span>Mon - Fri</span><span>8:00 AM - 6:00 PM</span></div>
    <div class="hours" style="top:300px"><span>Saturday</span><span>9:00 AM - 5:00 PM</span></div>
    <div class="hours" style="top:356px;border:none"><span>Sunday</span><span>Closed</span></div>
    <h4 style="top:410px">Recent Posts</h4>
    <div class="post" style="top:447px"><div class="thumb" role="img" aria-label="Thumbnail photo of a plumber at work"></div><div><b>Revitalising Your People In To a Retail Sown-turn.</b><small>▦ Apr 05 2024</small></div></div>
    <div class="post" style="top:532px"><div class="thumb" role="img" aria-label="Thumbnail photo of a plumber fixing a sink"></div><div><b>Revitalising Your People In To a Retail Sown-turn.</b><small>▦ Mar 14 2024</small></div></div>
    <div class="hr" style="top:640px"></div>
    <div class="links"><span>Setting &amp; Privacy</span><span>FAQ</span><span>Support</span></div>
    <div class="copy">Copyright © All Rights Reserved.</div>
    <div class="totop"><svg width="14" height="14" viewBox="0 0 14 14" fill="none" stroke="#3d84f5" stroke-width="1.5"><path d="M7 12V2M3 6l4-4 4 4"/></svg></div>
  </section>
</div>

</body>
</html>
```